Business Card Design Project

Build kick ass business card.
Updates

I just uploaded the Veruxo Logo in AI format, for those that were asking. It's looking real good and we'll be reviewing the designs soon. Thanks. 

Target Market(s)

Businesses in many verticals. Focusing on information security.

Veruxo, LLC
Darren Colby
Principal Security Consultant
Mobile: +1-480-555-0137
Email: Darren.Colby@Veruxo.example
Web: www.veruxo.example

Industry/Entity Type

Business

Requirements
Must have
• Design must look high-end, hi-tech stylish and minimalist

Be different – one that stands out from thousands of others

Does not have to be traditional rectangle

Would like logo integrated

```html
<!DOCTYPE html>
<html lang="en">
<head>
<meta charset="utf-8">
<title>Veruxo, LLC – Business Card</title>
<link rel="stylesheet" href="https://fonts.googleapis.com/css2?family=Arimo:ital,wght@0,400;1,700&display=swap">
<style>
  :root {
    --card-teal: #238a72;
    --grid-line: rgba(220, 235, 230, 0.55);
    --frame-grey: #76786f;
    --panel-white: #fbfbf9;
    --brand-ink: #1f1f1f;
    --accent-blue: #2a9fd6;
    --text-white: #ffffff;
  }
  * { margin: 0; padding: 0; box-sizing: border-box; }
  html, body {
    width: 1200px;
    height: 720px;
    overflow: hidden;
    background: var(--card-teal);
  }
  .card {
    position: relative;
    width: 1200px;
    height: 720px;
    background: var(--card-teal);
    font-family: "Arimo", Arial, sans-serif;
    color: var(--text-white);
    overflow: hidden;
  }
  .card-grid {
    position: absolute;
    inset: 0;
  }
  .brand-frame {
    position: absolute;
    left: 469px;
    top: 45px;
    width: 692px;
    height: 300px;
    background: var(--frame-grey);
    box-shadow: 0 6px 18px 6px rgba(200, 205, 200, 0.55);
  }
  .brand-panel {
    position: absolute;
    left: 20px;
    top: 18px;
    right: 16px;
    bottom: 19px;
    background: var(--panel-white);
    display: flex;
    align-items: center;
    justify-content: center;
    gap: 24px;
  }
  .brand-dot {
    width: 44px;
    height: 44px;
    border-radius: 50%;
    background: var(--accent-blue);
  }
  .brand-name {
    font-size: 44px;
    font-weight: 400;
    color: var(--brand-ink);
    line-height: 1;
  }
  .identity {
    position: absolute;
    left: 63px;
    top: 137px;
    font-size: 26.5px;
    font-weight: 700;
    font-style: italic;
    line-height: 37px;
  }
  .contact {
    position: absolute;
    left: 150px;
    top: 609px;
    font-size: 30px;
    line-height: 35px;
  }
</style>
</head>
<body>
  <main class="card">
    <svg class="card-grid" width="1200" height="720" viewBox="0 0 1200 720" aria-hidden="true">
      <g stroke="var(--grid-line)" stroke-width="2">
        <line x1="0" y1="14" x2="1200" y2="14"/>
        <line x1="0" y1="249" x2="1200" y2="249"/>
        <line x1="0" y1="484" x2="1200" y2="484"/>
        <line x1="299" y1="0" x2="299" y2="720"/>
        <line x1="593" y1="0" x2="593" y2="720"/>
        <line x1="889" y1="0" x2="889" y2="720"/>
      </g>
    </svg>

    <div class="brand-frame">
      <div class="brand-panel">
        <span class="brand-dot"></span>
        <span class="brand-name">Veruxo</span>
      </div>
    </div>

    <div class="identity">
      <p class="company">Veruxo, LLC</p>
      <p class="person">Darren Colby</p>
      <p class="role">Principal Security Consultant</p>
    </div>

    <div class="contact">
      <p>Mobile: +1-480-555-0137, Email: Darren.Colby@Veruxo.example</p>
      <p>Web: www.veruxo.example</p>
    </div>
  </main>
</body>
</html>
```